Update shopping site

Our current shopping website is outdated and we are wanting to update our shopping site to have a fresh new look/design.

Create a Web Design (Uncoded - PSD layout only)

We want you to develop the design for 4 pages:
1) Home Page
2) Remedy Type
3) Health Condition
4) Consultations

www.fernlowmeadow.com

Reason: Close to choosing design and a few missing items to be resolved.

Industry/Entity Type

Shopping

```html
<!DOCTYPE html>
<html lang="en">
<head>
<meta charset="utf-8">
<title>Fernlow Meadow – Nature for Life</title>
<link href="https://fonts.googleapis.com/css2?family=Open+Sans:wght@400;600&display=swap" rel="stylesheet">
<style>
:root{
  --green:#4b7a12;
  --green-dark:#3d6a0c;
  --text:#222;
  --muted:#888;
  --rule:#d8d8d8;
  --band:#f4f4f4;
  --price:#e5505b;
  --footer:#222;
  --footer-text:#ddd;
  --white:#fff;
}
*{margin:0;padding:0;box-sizing:border-box}
html,body{width:1200px;height:2597px;overflow:hidden}
body{position:relative;background:var(--white);font-family:"Open Sans",sans-serif;color:var(--text)}
.abs{position:absolute}
.header-search{left:95px;top:34px;font-size:16px;display:flex;align-items:center;gap:8px}
.brand{left:470px;top:22px;display:flex;align-items:center;gap:10px;color:var(--green);font-size:20px;line-height:22px}
.brand-mark{width:44px;height:44px;border-radius:50%;border:2px solid var(--green)}
.cart{right:88px;top:34px;font-size:16px;display:flex;align-items:center;gap:8px}
.header-rule{left:90px;top:90px;width:1022px;height:1px;background:var(--rule)}
.nav{left:90px;top:106px;width:1022px;display:flex;justify-content:space-between;font-size:16px}
.nav a{color:var(--text);text-decoration:none}
.nav a.active{color:var(--green)}
.hero{left:0;top:149px;width:1200px;height:516px;background:linear-gradient(100deg,#7a5a4a 0%,#b07a3e 25%,#6b5a66 50%,#c9b8b0 70%,#5a4a58 100%)}
.hero-title{right:176px;top:350px;text-align:right;color:var(--white);font-weight:600;line-height:1.05}
.hero-title .t1{font-size:58px}
.hero-title .t2{font-size:54px;font-weight:400}
.hero-arrow{top:418px;width:26px;height:26px;border-radius:50%;background:#222;display:flex;align-items:center;justify-content:center}
.section-title{left:0;width:1200px;text-align:center;font-size:31px;font-weight:400}
.intro{left:126px;top:798px;width:948px;text-align:center;font-size:13.5px;line-height:22px;color:#555}
.feature{width:280px;text-align:center}
.feature .ph{width:180px;height:180px;border-radius:50%;margin:0 auto;border:4px solid var(--white);box-shadow:0 0 0 1px #ddd}
.feature h3{font-weight:400;font-size:19px;margin-top:34px}
.feature p{font-size:13px;color:var(--muted);line-height:22px;margin-top:12px}
.band{left:0;top:1281px;width:1200px;height:554px;background:var(--band)}
.card{top:1429px;width:240px;height:296px;background:var(--white);box-shadow:0 1px 4px rgba(0,0,0,.2);text-align:center}
.card .ph{width:112px;height:155px;margin:13px auto 0;background:linear-gradient(#f4f0ec,#e6ded6);position:relative}
.card .ph span{position:absolute;left:38px;top:30px;width:36px;height:110px;border-radius:8px;background:linear-gradient(#2a2a2a,#4a3a30)}
.card .name{font-size:14px;margin-top:22px}
.card .prices{margin-top:6px;font-size:13px}
.card .was{color:var(--muted);text-decoration:line-through;margin-right:8px}
.card .now{color:var(--price);font-size:18px}
.card .btn{display:inline-block;margin-top:6px;width:104px;height:28px;line-height:28px;border-radius:14px;background:var(--green);color:var(--white);font-size:12px}
.band-arrow{top:1545px}
.event{top:2019px;display:flex;gap:14px;width:500px}
.event .ph{flex:0 0 163px;height:142px}
.event h4{font-weight:400;font-size:14px;margin-top:8px}
.event .date{font-size:13px;margin-top:8px}
.event p{font-size:12.5px;line-height:19px;color:#555;margin-top:6px}
.event .more{font-size:12px;color:var(--green);margin-top:8px;display:block}
.footer{left:0;top:2255px;width:1200px;height:342px;background:var(--footer);color:var(--footer-text)}
.fcol{top:2318px;font-size:12px}
.fcol h5{font-weight:400;font-size:14px;margin-bottom:12px;color:var(--white)}
.fcol li{list-style:none;line-height:23.5px}
.fcol li::before{content:"» ";}
.social{display:flex;gap:12px;margin-top:16px}
.social span{width:24px;height:24px;background:var(--footer-text);border-radius:4px}
.footer-rule{left:95px;top:2471px;width:1017px;height:1px;background:#3a3a3a}
.pay{left:468px;top:2510px;display:flex;gap:4px}
.pay span{width:49px;height:27px;border-radius:2px}
.copy{left:0;top:2550px;width:1200px;text-align:center;font-size:12px;color:var(--white)}
</style>
</head>
<body>
<div class="abs header-search">
  <svg width="14" height="14" viewBox="0 0 14 14"><circle cx="6" cy="6" r="4.5" fill="none" stroke="#4b7a12" stroke-width="2"/><line x1="9.5" y1="9.5" x2="13" y2="13" stroke="#4b7a12" stroke-width="2"/></svg>
  Search
</div>
<div class="abs brand"><span class="brand-mark"></span><span>Welcome to Fernlow Meadow<br>Nature for Life</span></div>
<div class="abs cart">
  <svg width="16" height="14" viewBox="0 0 16 14"><path d="M0 1h3l2 8h9l2-6H4" fill="none" stroke="#4b7a12" stroke-width="2"/><circle cx="6" cy="12" r="1.5" fill="#4b7a12"/><circle cx="13" cy="12" r="1.5" fill="#4b7a12"/></svg>
  Cart : 0
</div>
<div class="abs header-rule"></div>
<nav class="abs nav">
  <a class="active" href="#">Home</a><a href="#">Remedy Type</a><a href="#">Health Condition</a><a href="#">Accessories &amp; Supplies</a><a href="#">Loyalty Program</a><a href="#">Contact Us</a>
</nav>

<div class="abs hero" role="img" aria-label="Glass bottle of herbal tincture beside a mortar and dried flowers"></div>
<div class="abs hero-title"><div class="t1">FERNLOW MEADOW</div><div class="t2">Nature for life</div></div>
<div class="abs hero-arrow" style="left:68px"><svg width="10" height="10"><path d="M7 1L3 5l4 4" fill="none" stroke="#fff" stroke-width="2"/></svg></div>
<div class="abs hero-arrow" style="left:1103px"><svg width="10" height="10"><path d="M3 1l4 4-4 4" fill="none" stroke="#fff" stroke-width="2"/></svg></div>

<h2 class="abs section-title" style="top:745px">Welcome to Fernlow Meadow</h2>
<p class="abs intro">We offer some of the best botanical health care products in our industry (we require certificate of Analysis from our suppliers to ensure the purity of our product, that it is free of pesticides, contaminants, mold, fungus and it is the right product); we have over 300 NPN (Natural Product Number) licenses approved by the national health authority and our friendly staff is well qualified to answer most questions you may have.</p>

<div class="abs feature" style="left:111px;top:911px">
  <div class="ph" role="img" aria-label="Bowls of dried herbs and seeds" style="background:radial-gradient(#8a6a4a,#4a3a2a)"></div>
  <h3>Remedies</h3><p>It has survived not only five centuries,<br>but also the leap into electronic</p>
</div>
<div class="abs feature" style="left:456px;top:911px">
  <div class="ph" role="img" aria-label="Fresh green herbs in a mortar" style="background:radial-gradient(#9bbf6a,#d8dcc8)"></div>
  <h3>Health Condition</h3><p>It has survived not only five centuries,<br>but also the leap into electronic</p>
</div>
<div class="abs feature" style="left:797px;top:911px">
  <div class="ph" role="img" aria-label="Small oil bottles among herbs" style="background:radial-gradient(#c8c080,#6a8a4a)"></div>
  <h3>Herbal</h3><p>It has survived not only five centuries,<br>but also the leap into electronic</p>
</div>

<div class="abs band"></div>
<h2 class="abs section-title" style="top:1344px">Featured Products</h2>
<svg class="abs band-arrow" style="left:56px" width="22" height="36"><path d="M20 2L3 18l17 16" fill="none" stroke="#aaa" stroke-width="2"/></svg>
<svg class="abs band-arrow" style="left:1122px" width="22" height="36"><path d="M2 2l17 16L2 34" fill="none" stroke="#aaa" stroke-width="2"/></svg>

<div class="abs card" style="left:92px"><div class="ph" role="img" aria-label="Amber dropper bottle"><span></span></div><div class="name">Product Name</div><div class="prices"><span class="was">$659.00</span><span class="now">$599.99</span></div><span class="btn">BUY NOW</span></div>
<div class="abs card" style="left:350px"><div class="ph" role="img" aria-label="Amber dropper bottle"><span></span></div><div class="name">Product Name</div><div class="prices"><span class="was">$659.00</span><span class="now">$599.99</span></div><span class="btn">BUY NOW</span></div>
<div class="abs card" style="left:608px"><div class="ph" role="img" aria-label="Amber dropper bottle"><span></span></div><div class="name">Product Name</div><div class="prices"><span class="was">$659.00</span><span class="now">$599.99</span></div><span class="btn">BUY NOW</span></div>
<div class="abs card" style="left:867px"><div class="ph" role="img" aria-label="Amber dropper bottle"><span></span></div><div class="name">Product Name</div><div class="prices"><span class="was">$659.00</span><span class="now">$599.99</span></div><span class="btn">BUY NOW</span></div>

<h2 class="abs section-title" style="top:1927px">Upcoming Events</h2>
<div class="abs event" style="left:88px">
  <div class="ph" role="img" aria-label="Spoons of dried herbs and spices" style="background:linear-gradient(135deg,#6a5030,#b89a60)"></div>
  <div><h4>Nemo Enim Ipsam Volup</h4><div class="date">09-07-2017</div><p>It has survived not only five centuries, but also the leap into electronic typesetting, remaining essentially unchanged. It was popularised</p><span class="more">Read More &gt;&gt;</span></div>
</div>
<div class="abs event" style="left:627px">
  <div class="ph" role="img" aria-label="White daisies with homeopathic pills" style="background:linear-gradient(135deg,#9a9a9a,#e8e8e0)"></div>
  <div><h4>Nemo Enim Ipsam Volup</h4><div class="date">09-07-2017</div><p>It has survived not only five centuries, but also the leap into electronic typesetting, remaining essentially unchanged. It was popularised</p><span class="more">Read More &gt;&gt;</span></div>
</div>

<footer class="abs footer"></footer>
<div class="abs fcol" style="left:95px"><h5>INFORMATION</h5><ul><li>Privacy Policy</li><li>Your Account</li><li>Advanced Search</li><li>Contact Us</li></ul></div>
<div class="abs fcol" style="left:336px"><h5>CUSTOMER SERVICE</h5><ul><li>Safe Shopping Guarantee</li><li>Shipping Rates</li><li>Returns</li><li>Return Policy</li></ul></div>
<div class="abs fcol" style="left:623px;line-height:23.5px"><h5>CONTACT US</h5>Address : Thistle Farm, Kiln Road<br>Aldercombe, Canada<br>Phone : 01632960418<br>Email : hello@fernlowmeadow.com</div>
<div class="abs fcol" style="left:937px;top:2312px"><h5>FOLLOW US OUT THERE</h5><div class="social"><span></span><span></span><span></span><span></span></div></div>
<div class="abs footer-rule"></div>
<div class="abs pay"><span style="background:#2a7ab8"></span><span style="background:#7a2a6a"></span><span style="background:#1a3a8a"></span><span style="background:#e87a20"></span><span style="background:#f0f0f0"></span></div>
<div class="abs copy">Copyright © 2017. All Rights Reserved</div>
</body>
</html>
```